Internet Of Things brochure

Need to create a brochure with a common theme to our website and the last 2 pages of the attached file. All the contect is in the file that I have attached.
website www.norvalenetworks.com.au

Industry/Entity Type

Internet

```html
<!DOCTYPE html>
<html lang="en">
<head>
<meta charset="utf-8">
<title>Norvale Networks – Internet of Things Brochure</title>
<link href="https://fonts.googleapis.com/css2?family=Titillium+Web:wght@400;600;700&family=Open+Sans:wght@400;600;700&display=swap" rel="stylesheet">
<style>
:root{
  --bg:#e4e5e7;
  --paper:#ffffff;
  --navy:#1d3a73;
  --blue:#2b5797;
  --sky:#4f7fc0;
  --purple:#4b2a72;
  --plum:#5e2f7e;
  --ink:#3a3a48;
  --muted:#6b6b78;
  --light:#dfe6f2;
}
*{box-sizing:border-box;margin:0;padding:0}
html,body{width:1200px;height:1000px;overflow:hidden;background:var(--bg)}
body{position:relative;font-family:"Open Sans",Arial,sans-serif;color:var(--ink)}
.spread{position:absolute;left:255px;width:690px;height:488px;display:flex;box-shadow:0 6px 18px rgba(0,0,0,.18)}
.spread--inside{top:6px}
.spread--outside{top:506px}
.page{position:relative;width:345px;height:488px;background:var(--paper);overflow:hidden}
.page + .page{border-left:1px solid #e6e6ea}
.h{font-family:"Titillium Web",Arial,sans-serif;font-weight:700;text-transform:uppercase;line-height:1.02}
.body{font-size:4.6px;line-height:1.45;color:var(--ink)}
.body p{margin-bottom:3px}
.photo{position:absolute}
.abs{position:absolute}

/* inside left */
.hero-tablet{left:0;top:0;width:345px;height:205px;background:linear-gradient(135deg,#c9d3e2 0%,#8ea1bf 40%,#3f5275 75%,#2a3552 100%)}
.chevron{position:absolute;left:0;top:110px}
.chevron-title{left:14px;top:170px;color:#fff;font-size:13px;width:100px}
.dna{left:140px;top:214px;width:190px}
.dna strong{display:block;font-size:5px;color:var(--navy);margin-bottom:3px}
.rule{left:14px;right:14px;top:335px;height:1px;background:#d9d9e0}
.age-title{left:18px;top:360px;color:var(--purple);font-size:13px;width:110px}
.age-text{left:140px;top:348px;width:190px}
.age-text ul{list-style:none;margin-bottom:3px}

/* inside right */
.band{left:0;top:0;width:345px;height:38px;background:linear-gradient(90deg,var(--plum),var(--navy))}
.band-title{left:22px;top:12px;color:#fff;font-size:12px;letter-spacing:.3px}
.cities-text{left:16px;top:52px;width:140px}
.smart-grid{left:168px;top:50px;width:165px;display:grid;grid-template-columns:1fr 1fr;gap:10px 8px}
.smart{display:flex;gap:4px}
.smart-icon{flex:0 0 11px;height:11px;border:1px solid var(--navy);border-radius:50%}
.smart h4{font-family:"Titillium Web",sans-serif;font-size:5px;color:var(--navy);text-transform:uppercase;line-height:1}
.smart p{font-size:4.3px;line-height:1.4;color:var(--muted)}
.help-title{left:16px;top:268px;width:140px;font-family:"Titillium Web",sans-serif;font-weight:700;font-size:7px;color:var(--purple);line-height:1.1}
.help-text{left:16px;top:292px;width:140px}
.help-text ul{padding-left:6px}
.stack{left:166px;top:262px}
.stack text{font-family:"Open Sans",Arial,sans-serif}
.stack .layer{font-size:5.2px;font-weight:700;fill:#fff}
.stack .layer-sub{font-size:4.2px;fill:#e6edf8}
.stack .side{font-size:4.4px;font-weight:700;fill:#fff;letter-spacing:.2px}
.stack .tier{font-size:4.4px;font-weight:700;fill:var(--navy)}
.stack .cap{font-size:5px;font-weight:700;fill:var(--purple)}

/* outside left */
.cities-panel{left:0;top:0;width:345px;height:300px;background:linear-gradient(180deg,#2c4d86 0%,var(--navy) 45%,#1a2f5f 100%)}
.panel-title{left:22px;top:22px;color:#fff;font-size:13px}
.features{left:22px;top:60px;width:305px;display:grid;grid-template-columns:repeat(3,1fr);gap:14px 10px}
.feature h4{font-family:"Titillium Web",sans-serif;font-size:5px;color:#fff;text-transform:uppercase;margin-bottom:2px;line-height:1.1}
.feature p{font-size:4.4px;line-height:1.45;color:#d6def0;margin-bottom:2px}
.workshop{left:0;top:300px;width:345px;height:142px;background:linear-gradient(90deg,var(--purple),#3d2f70)}
.workshop-title{left:22px;top:312px;color:#fff;font-size:9px;width:130px}
.workshop-text{left:22px;top:336px;width:130px;font-size:4.4px;line-height:1.45;color:#e4dcef}
.meeting{left:160px;top:300px;width:185px;height:142px;background:linear-gradient(135deg,#d8dde6,#a9b3c4 50%,#6d7890)}
.footer{left:0;top:442px;width:345px;height:46px;background:#fff;display:flex;align-items:center;padding:0 22px;gap:16px}
.brand{display:flex;align-items:center;gap:4px;font-family:"Titillium Web",sans-serif;font-weight:700;font-size:9px;color:var(--navy)}
.brand-mark{width:9px;height:9px;background:var(--navy)}
.badge{width:22px;height:12px;background:var(--light)}
.badge--blue{width:12px;background:var(--sky)}
.address{margin-left:auto;font-size:4.6px;line-height:1.45;color:var(--ink)}
.address b{color:var(--navy)}

/* outside right */
.topbar{left:0;top:0;width:345px;height:56px;display:flex;align-items:center;padding:0 22px;gap:10px}
.topbar .brand{font-size:11px}
.topbar .brand-mark{width:11px;height:11px}
.topbar .badges{margin-left:auto;display:flex;gap:8px;align-items:center}
.hero-team{left:0;top:56px;width:345px;height:244px;background:linear-gradient(120deg,#e7e9ee 0%,#b8c1d0 45%,#5d6a84 80%,#34405a 100%)}
.enable-shape{position:absolute;left:0;top:180px}
.enable-title{left:22px;top:232px;color:#fff;font-size:11px;width:100px}
.services{left:0;top:300px;width:345px;height:188px;background:linear-gradient(160deg,#2a4c86 0%,#33407a 50%,var(--purple) 100%)}
.lead{left:22px;top:312px;width:170px;font-size:5.2px;font-weight:700;color:#fff;line-height:1.35}
.services-text{left:22px;top:338px;width:150px;font-size:4.4px;line-height:1.45;color:#dbe2f1}
.services-text p{margin-bottom:3px}
.svc-cols{left:185px;top:338px;width:150px;display:grid;grid-template-columns:1fr 1fr;gap:8px 8px}
.svc h5{font-family:"Titillium Web",sans-serif;font-size:4.8px;color:#fff;text-transform:uppercase;margin-bottom:1px}
.svc li{list-style:none;font-size:4.3px;line-height:1.45;color:#dbe2f1}
.cta{left:22px;top:454px;font-size:5.2px;font-weight:700;color:#fff;line-height:1.4}
</style>
</head>
<body>

<!-- Inside spread -->
<section class="spread spread--inside">
  <div class="page">
    <div class="photo hero-tablet" role="img" aria-label="Businessman holding a tablet showing charts"></div>
    <svg class="chevron" width="125" height="185" viewBox="0 0 125 185" aria-hidden="true">
      <polygon points="0,0 125,45 125,135 62,185 0,160" fill="#4b2a72" opacity=".95"/>
    </svg>
    <h2 class="h abs chevron-title">Embrace digital or risk being left behind</h2>
    <div class="abs body dna">
      <strong>Does your business have the Digital DNA required to succeed in the digital era?</strong>
      <p>Embracing the new revolution in digital technology is more than just having an online presence. It is about using connected tools in every part of your business, from how you reach customers to how you run daily operations and measure results.</p>
      <p>The way business operates has been deeply changed by advancements in digital technology. Integrated systems allow for better sharing of data, smarter decisions and faster service. Companies that adapt early gain a clear edge in cost, speed and customer loyalty.</p>
      <p>Many enterprises have been slow to make the change. Through our integrated services we help you move forward with confidence and build a business that is ready for what comes next.</p>
    </div>
    <div class="abs rule"></div>
    <h2 class="h abs age-title">The age of digital distribution is here</h2>
    <div class="abs body age-text">
      <p>The world's largest taxi firm owns no vehicles. The world's largest accommodation provider owns no real estate. The world's most popular media owner creates no content. Something big is happening in how value is delivered.</p>
      <p>Creating and controlling the marketplace between the consumer and the product is where value is created today. Ask yourself:</p>
      <ul>
        <li>• Is your business capable of responding quickly to digital trends?</li>
        <li>• Are you doing all you can to compete in the digital economy?</li>
        <li>• Does your business continue to grow in value in the face of change?</li>
      </ul>
      <p>Norvale Digital works closely with you to identify new opportunities, improve your processes and prepare your business for the next wave of digital growth.</p>
    </div>
  </div>

  <div class="page">
    <div class="abs band"></div>
    <h2 class="h abs band-title">Smart Cities Initiative</h2>
    <div class="abs body cities-text">
      <p>A smart city is an urban development vision to integrate information and communication technology and Internet of Things solutions to manage a city's assets. These assets include local departments, information systems, schools, libraries, transport networks, hospitals, power plants, water supply, waste management, law enforcement and other community services.</p>
      <p>The goal of building a smart city is to improve quality of life by using technology to improve the efficiency of services and meet residents' needs. Sensors collect data in real time, which is used to manage assets and resources well and respond to challenges as they arise.</p>
      <p>Norvale Digital has partnered with our network and cloud partners to bring these solutions to local councils, developers and service providers across the region.</p>
    </div>
    <div class="abs smart-grid">
      <div class="smart"><span class="smart-icon"></span><div><h4>Smart governance</h4><p>Interconnected and open services for better planning between public and private sectors.</p></div></div>
      <div class="smart"><span class="smart-icon"></span><div><h4>Smart environment</h4><p>Energy saving, renewables, pollution control and monitoring, green buildings and planning.</p></div></div>
      <div class="smart"><span class="smart-icon"></span><div><h4>Smart economy</h4><p>ICT-enabled production, manufacturing and delivery of services and new business models.</p></div></div>
      <div class="smart"><span class="smart-icon"></span><div><h4>Smart people</h4><p>Digital skills, learning and access to education, human resources and capacity building.</p></div></div>
      <div class="smart"><span class="smart-icon"></span><div><h4>Smart mobility</h4><p>ICT supported and integrated transport and logistics, suitable safe and sustainable systems.</p></div></div>
      <div class="smart"><span class="smart-icon"></span><div><h4>Smart living</h4><p>ICT-enabled lifestyles, behaviour and health, safe and culturally vibrant cities.</p></div></div>
    </div>
    <h3 class="abs help-title">How we help you get the most from your IoT and M2M solutions</h3>
    <div class="abs body help-text">
      <p>We are committed to delivering connected solutions that transform business productivity. We deliver agile, reliable platforms to drive real results.</p>
      <p>Our commitment is demonstrated through:</p>
      <ul>
        <li>Tailored, scalable network options</li>
        <li>Ongoing investment in services and platforms</li>
        <li>Continued focus on emerging technology</li>
        <li>Support dedicated to customer success</li>
      </ul>
    </div>
    <svg class="abs stack" width="170" height="216" viewBox="0 0 170 216" role="img" aria-label="IoT solution architecture: five layers from devices up to applications, framed by security, device management and managed services">
      <text class="cap" x="0" y="7">End-to-end IoT architecture</text>
      <!-- vertical capability bars -->
      <rect x="0" y="14" width="9" height="200" fill="#4b2a72"/>
      <rect x="11" y="14" width="9" height="200" fill="#5e2f7e"/>
      <rect x="22" y="14" width="9" height="200" fill="#7a5a98"/>
      <text class="side" transform="translate(6.3 210) rotate(-90)">SECURITY &amp; COMPLIANCE</text>
      <text class="side" transform="translate(17.3 210) rotate(-90)">DEVICE MANAGEMENT</text>
      <text class="side" transform="translate(28.3 210) rotate(-90)">MANAGED SERVICES &amp; SUPPORT</text>
      <!-- stacked layers -->
      <rect x="34" y="14" width="100" height="36" fill="#2b5797"/>
      <text class="layer" x="39" y="27">Applications</text>
      <text class="layer-sub" x="39" y="35">Dashboards, mobile apps</text>
      <text class="layer-sub" x="39" y="42">and business systems</text>

      <rect x="34" y="54" width="100" height="36" fill="#3a68a8"/>
      <text class="layer" x="39" y="67">Analytics &amp; insights</text>
      <text class="layer-sub" x="39" y="75">Reporting, alerts and</text>
      <text class="layer-sub" x="39" y="82">predictive models</text>

      <rect x="34" y="94" width="100" height="36" fill="#4f7fc0"/>
      <text class="layer" x="39" y="107">Cloud IoT platform</text>
      <text class="layer-sub" x="39" y="115">Data ingestion, storage</text>
      <text class="layer-sub" x="39" y="122">and integration</text>

      <rect x="34" y="134" width="100" height="36" fill="#6b93cc"/>
      <text class="layer" x="39" y="147">Network &amp; connectivity</text>
      <text class="layer-sub" x="39" y="155">4G, NB-IoT, LoRaWAN</text>
      <text class="layer-sub" x="39" y="162">and Wi-Fi</text>

      <rect x="34" y="174" width="100" height="40" fill="#8eacd8"/>
      <text class="layer" x="39" y="187">Sensors &amp; devices</text>
      <text class="layer-sub" x="39" y="195">Meters, vehicles, buildings</text>
      <text class="layer-sub" x="39" y="202">and field equipment</text>

      <!-- tier labels -->
      <rect x="137" y="14" width="31" height="36" fill="#dfe6f2"/>
      <text class="tier" x="152.5" y="34" text-anchor="middle">BUSINESS</text>
      <rect x="137" y="54" width="31" height="76" fill="#dfe6f2"/>
      <text class="tier" x="152.5" y="94" text-anchor="middle">DATA</text>
      <rect x="137" y="134" width="31" height="80" fill="#dfe6f2"/>
      <text class="tier" x="152.5" y="176" text-anchor="middle">THINGS</text>
    </svg>
  </div>
</section>

<!-- Outside spread -->
<section class="spread spread--outside">
  <div class="page">
    <div class="abs cities-panel" role="img" aria-label="Faint city skyline behind a deep blue panel"></div>
    <h2 class="h abs panel-title">Smart Cities Initiative</h2>
    <div class="abs features">
      <div class="feature"><h4>Innovate and transform your business with IoT solutions</h4><p>Put the Internet of Things to work for you. Drive digital transformation across your business with end-to-end solutions that can be tailored to your needs, helping make informed decisions, cut operating costs and create new revenue streams.</p></div>
      <div class="feature"><h4>Remote monitoring</h4><p>Reduce manual, time-intensive processes when you connect and monitor your business devices and assets. Access, analyse and use data to prevent failures, automate processes and trigger alerts and actions, such as remote diagnostics.</p></div>
      <div class="feature"><h4>Connected vehicle</h4><p>Transform the driving experience while innovating automotive services with the Norvale connected vehicle platform. Combine predictive services and driver assistance to create new differentiated experiences that increase loyalty and revenue.</p></div>
      <div class="feature"><h4>Connected field service</h4><p>Detect, troubleshoot and resolve issues remotely before your customers know there's a problem.</p><p>When an issue escalates, automatically dispatch the best technician and tools to deliver a first-time fix.</p></div>
      <div class="feature"><h4>Predictive maintenance</h4><p>Anticipate your maintenance needs to prevent equipment failures and avoid unscheduled downtime. Analyse incoming data to quickly assess conditions, recognise warning signs and proactively service equipment before costly repairs are needed.</p></div>
      <div class="feature"><h4>Smart buildings</h4><p>Reduce costs, improve efficiencies and increase occupant satisfaction and productivity using IoT. Gain actionable insights and control by connecting building devices and systems, collecting data and running powerful analytics.</p></div>
    </div>
    <div class="abs workshop"></div>
    <h2 class="h abs workshop-title">Request a Digital Discovery Workshop</h2>
    <div class="abs workshop-text">The Digital Discovery Workshop is a half day opportunity for the key stakeholders of your business that allows Norvale Digital to identify the problems facing your business and how best to address them through a digital transformation. During this workshop you will understand the investment the digital environment may present to your business and the opportunities that exist by applying digital solutions to your business. We also provide our clients with the opportunity to consider the overall strategy and actions needed to reach the goals set by the meeting. This analysis is relevant to all business types and industries.</div>
    <div class="photo meeting" role="img" aria-label="Team meeting around a table in a bright office"></div>
    <div class="abs footer">
      <div class="brand"><span class="brand-mark"></span>Norvale Networks</div>
      <span class="badge"></span><span class="badge"></span><span class="badge badge--blue"></span>
      <div class="address">127 Carrow Road<br>Lidmore, NSW 2190<br>P: 1300 555 019<br><b>www.norvalenetworks.com.au</b></div>
    </div>
  </div>

  <div class="page">
    <div class="abs topbar">
      <div class="brand"><span class="brand-mark"></span>Norvale Networks</div>
      <div class="badges"><span class="badge"></span><span class="badge"></span><span class="badge badge--blue"></span></div>
    </div>
    <div class="photo hero-team" role="img" aria-label="Two businessmen reviewing work on a laptop"></div>
    <svg class="enable-shape" width="160" height="120" viewBox="0 0 160 120" aria-hidden="true">
      <polygon points="0,40 105,0 160,120 0,120" fill="#4b2a72" opacity=".92"/>
    </svg>
    <h2 class="h abs enable-title">Enable your business</h2>
    <div class="abs services"></div>
    <p class="abs lead">We can provide digital solutions across all parts of the business model and are completely tailored to your business or industry.</p>
    <div class="abs services-text">
      <p>We can cover the following scenarios:</p>
      <p>Introduce a digitally strategic business model, digitising operations and processes by leveraging cloud-based applications and mobile devices that digitise data collection, collection and supply chain processes.</p>
      <p>Learning and development solutions that comprise an array of digital tools that are always available via the cloud, built in minutes, and completely customisable.</p>
      <p>Seamlessly integrating digital commerce into your existing online and mobile business to help you compete effectively.</p>
      <p>Creating targeted and measurable digital marketing campaigns that focus on increasing first-time and repeat sales and building long-term loyalty.</p>
    </div>
    <div class="abs svc-cols">
      <div class="svc"><h5>Digital commerce</h5><ul><li>&gt; eCommerce</li><li>&gt; mCommerce</li><li>&gt; Digital payment integration</li></ul></div>
      <div class="svc"><h5>Digital learning</h5><ul><li>&gt; Cloud LMS</li><li>&gt; Learning and development solutions</li><li>&gt; Compliance Cloud</li></ul></div>
      <div class="svc"><h5>Digital business solutions</h5><ul><li>&gt; Cloud ERP, CRM, SCM, HCM</li><li>&gt; IoT integration to ERP, CRM, SCM</li><li>&gt; Digital workflow solutions</li><li>&gt; Any device ERP, CRM, SCM</li></ul></div>
      <div class="svc"><h5>Digital marketing</h5><ul><li>&gt; SEO &amp; SEM</li><li>&gt; Marketing insights and analytics</li><li>&gt; Responsive EDMs and digital campaigns</li><li>&gt; Digital CTA</li><li>&gt; Proximity marketing</li></ul></div>
    </div>
    <p class="abs cta">Interested in discovering you digital opportunities?<br>Let's talk – 1300 555 019</p>
  </div>
</section>

</body>
</html>
```